Harbour Green Rink Events - Flyer

So now that i have the logo, I need a flyer made up for printing to be delivered to businesses and residential homes.
Below is some information that I want included in the design, in any order and in anyway.
What better way to spend time with family, friends or workmates then to enjoy 2 hours of barefoot bowls.
We can cater for Xmas Parties, Buck's and Hen's Parties, Birthday Parties, Team Building events.
We have food and drink packages to suit all your needs.
So why not come along and have the best fun you can have on 2 feet!
We have 2 locations at Wattlebrook Sports and Bowling Club and Merriden Bowling Club
Prices start from $12pp for 2 hours of lawn bowls fun
Contact Wade Kessler on 0482 157 394 or visit our website www.harbourgreenrinkevents.com.au for more information and to enquire about your function today!

```html
<!DOCTYPE html>
<html lang="en">
<head>
<meta charset="utf-8">
<title>Harbour Green Rink Events – Flyer</title>
<link rel="stylesheet" href="https://fonts.googleapis.com/css2?family=Fredoka:wght@600&family=Roboto+Condensed:wght@700&display=swap">
<style>
  :root {
    --sky-top: #1d6fc4;
    --sky-bottom: #35c3ef;
    --frame: #ffffff;
    --orange: #f37a21;
    --orange-light: #f58a3a;
    --red: #ec1c24;
    --green: #8dc63f;
    --fold: #4a4f55;
    --grass-top: #a6d94a;
    --grass-bottom: #3f8f1e;
    --white: #ffffff;
    --panel: rgba(255,255,255,0.88);
  }
  * { margin: 0; padding: 0; box-sizing: border-box; }
  html, body { width: 848px; height: 1200px; overflow: hidden; }
  body { font-family: "Roboto Condensed", Arial, sans-serif; }
  .flyer {
    position: relative;
    width: 848px; height: 1200px; overflow: hidden;
    background: linear-gradient(180deg, var(--sky-top) 0%, var(--sky-bottom) 70%);
  }
  .frame {
    position: absolute; left: 89px; top: 59px; width: 666px; height: 720px;
    background: var(--frame);
  }
  .frame-inner {
    position: absolute; left: 17px; top: 17px; right: 17px; bottom: 0;
    background: linear-gradient(180deg, var(--orange) 0%, var(--orange-light) 100%);
  }
  .headline {
    position: absolute; left: 30px; top: 66px; width: 510px; height: 124px;
    background: var(--red);
    transform: rotate(-8deg);
    box-shadow: 4px 10px 0 rgba(60,40,30,0.55);
    display: flex; align-items: center; justify-content: center;
    font-family: "Fredoka", "Arial Rounded MT Bold", sans-serif;
    color: var(--white); font-size: 25px; line-height: 1.05; text-align: center;
    padding: 0 18px;
    text-shadow: 1px 1px 1px rgba(0,0,0,0.4);
  }
  .photo {
    position: absolute; left: 520px; top: 24px; width: 305px; height: 220px;
    background: var(--white); padding: 12px;
    transform: rotate(8deg);
    box-shadow: 2px 4px 6px rgba(0,0,0,0.35);
  }
  .photo-fill {
    width: 100%; height: 100%;
    background: linear-gradient(160deg, #d9a88a 0%, #7cc24a 45%, #4aa02c 100%);
  }
  .note {
    position: absolute; background: var(--green); color: var(--white);
    font-size: 23px; line-height: 1.4; text-align: center;
    display: flex; align-items: center; justify-content: center;
    box-shadow: 3px 4px 4px rgba(0,0,0,0.3);
  }
  .note-events { left: 229px; top: 239px; width: 462px; height: 130px; }
  .note-food { left: 28px; top: 418px; width: 265px; height: 133px; }
  .note-fun { left: 464px; top: 443px; width: 337px; height: 129px; }
  .fold { position: absolute; }
  .locations {
    position: absolute; left: 106px; top: 612px; width: 620px;
    color: var(--white); font-size: 27px; line-height: 1.4; text-align: center;
  }
  .price {
    position: absolute; left: 534px; top: 705px; width: 257px; height: 139px;
    background: var(--red); color: var(--white);
    font-size: 28px; line-height: 1.33; text-align: center;
    display: flex; align-items: center; justify-content: center;
    box-shadow: 3px 4px 4px rgba(0,0,0,0.3);
  }
  .grass {
    position: absolute; left: 0; top: 738px; width: 848px; height: 462px;
    background: linear-gradient(180deg, var(--grass-top) 0%, #6cb833 35%, var(--grass-bottom) 100%);
  }
  .contact {
    position: absolute; left: 28px; top: 873px; width: 799px; height: 261px;
    background: var(--panel); border-radius: 28px;
    display: flex; align-items: center; justify-content: center;
    font-family: "Fredoka", "Arial Rounded MT Bold", sans-serif;
    color: var(--red); font-size: 38px; line-height: 1.16; text-align: center;
  }
</style>
</head>
<body>
<div class="flyer">
  <div class="frame"><div class="frame-inner"></div></div>

  <svg class="fold" style="left:28px;top:551px" width="61" height="36" viewBox="0 0 61 36"><polygon points="0,0 61,0 61,36" fill="var(--fold)"/></svg>
  <svg class="fold" style="left:755px;top:572px" width="46" height="34" viewBox="0 0 46 34"><polygon points="0,0 46,0 0,34" fill="var(--fold)"/></svg>
  <svg class="fold" style="left:755px;top:690px" width="36" height="15" viewBox="0 0 36 15"><polygon points="0,0 36,15 0,15" fill="var(--fold)"/></svg>

  <div class="headline">What better way to spend time with family, friends or workmates then to enjoy 2 hours of barefoot bowls.</div>

  <div class="photo"><div class="photo-fill" role="img" aria-label="Barefoot players bending to roll black bowls across a green lawn"></div></div>

  <div class="note note-events">We can cater for Xmas Parties, Buck's<br>and Hen's Parties, Birthday Parties,<br>Team Building events.</div>
  <div class="note note-food">We have food and<br>drink packages to<br>suit all your needs.</div>
  <div class="note note-fun">So why not come along<br>and have the best fun you<br>can have on 2 feet!</div>

  <div class="locations">We have 2 locations at Wattlebrook Sports and<br>Bowling Club and Merriden Bowling Club</div>

  <div class="grass" role="img" aria-label="Close-up of tall green grass blades"></div>

  <div class="price">Prices start from<br>$12pp for 2 hours<br>of lawn bowls fun</div>

  <div class="contact">Contact Wade Kessler on 0482 157 394<br>or visit our website<br>www.harbourgreenrinkevents.com.au<br>for more information and to enquire<br>about your function today!</div>
</div>
</body>
</html>
```